Broschüren-Design für Unternehmen aus dem Gesundheitsbereich
Zielgruppe
Wir sind ein Unternehmen aus dem Gesundheitsbereich und bieten wissenschaftlich fundierte Mikronährstoffanalysen (intravenöse Blutanalysen) an. Die Auswertung erfolgt mit Hilfe der weltweit einzigartigen Datenbank unseres wissenschaftlichen Leiters Prof. Dr. Torsten Halbach und beinhaltet zusätzliche eine individuelle Mikronährstoffempfehlung. Der Kunde kann unser Konzept in Form einer Analysebox (mit Materialien zur Entnahme von Blut- und Urinproben) bei uns erwerben. Es gibt verschiedene Analyseboxen in unterschiedlichem Umfang und Preisgestaltung zur Auswahl.
Unsere Zielgruppe sind gesundheitsbewusste Männer und Frauen im mittleren Alter („Gesundheitsmaximierer“).
Aufgabenstellung
8-12 Seiten, Format DIN A 5
Die Farbwahl bitte harmonisch an unser vorhandenes Logo / die angehängte Stylecard anpassen.
Die Neuauflage unserer Broschüre soll allgemeiner gehalten werden. Insbesondere die Titelseite (Bild sowie Headlines) der aktuellen Broschüre (siehe Upload) soll neugestaltet werden. Das Titelbild auf der Broschüre möchten wir gerne gegen allgemeineres Bildmaterial austauschen, z. B. mit Affinität zu unserem Logo oder zu den Themen Wissenschaft / Gesundheit / Mikronährstoffe. Seite 5 ('Die Analyse; Vier verschiedene Module') erfordert eine komplette Neugestaltung, da die angebotenen Analysemodule in der Form nicht mehr existieren. Wir haben neue themenspezifische Analyseboxen ins Leben gerufen (siehe Website: https://vitalquellnord.de/shop/), die wir allerdings nicht explizit in der Broschüre vorstellen möchten, damit die Broschüre bei möglichen Änderungen unseres Angebots künftig trotzdem immer aktuell bleibt. Aus diesem Grund wünschen wir uns für die Neuauflage der Broschüre durchweg allgemeingültige Formulierungen (Ohne Erwähnung von Namen oder Anzahl der angebotenen Analyseboxen).
Der Erklärfilm auf unserer Website verdeutlicht unser Konzept: https://www.videoportal-beispiel.de/watch?v=Qk3TzR8mLw2&feature=emb_title
Orientieren Sie sich gerne an den Creatives/Texten auf unserer Website.

```html
<!DOCTYPE html>
<html lang="de">
<head>
<meta charset="utf-8">
<title>Broschüre – Die Zukunft der Vorsorge</title>
<link rel="stylesheet" href="https://fonts.googleapis.com/css2?family=Exo+2:wght@300;400;600&display=swap">
<style>
  :root {
    --page-bg: #d6d6d6;
    --paper: #ffffff;
    --teal: #3fb3bd;
    --green-band: #8cbd3c;
    --photo-dark: #1f7f3a;
    --photo-mid: #3aa845;
    --photo-light: #7fd0a8;
    --white: #ffffff;
  }
  * { box-sizing: border-box; margin: 0; padding: 0; }
  html, body { width: 1200px; height: 902px; overflow: hidden; }
  body {
    background: var(--page-bg);
    font-family: "Exo 2", sans-serif;
    position: relative;
  }
  .cover {
    position: absolute;
    left: 310px; top: 41px;
    width: 580px; height: 820px;
    background: var(--paper);
    overflow: hidden;
    box-shadow: 0 6px 24px rgba(0,0,0,.18);
  }
  .cover-art { position: absolute; inset: 0; }
  .brand {
    position: absolute; left: 0; right: 0; top: 60px;
    display: flex; justify-content: center; align-items: center; gap: 14px;
  }
  .brand-dot {
    width: 40px; height: 40px; border-radius: 50%;
    background: var(--teal);
  }
  .brand-name {
    font-size: 42px; font-weight: 400; color: var(--teal);
    line-height: 1;
  }
  .headline {
    position: absolute; left: 96px; top: 420px;
    color: var(--white); font-size: 62px; font-weight: 300;
    line-height: 1.02;
  }
  .tagline-block {
    position: absolute; left: 60px; top: 690px;
    color: var(--white);
  }
  .tagline-main { font-size: 23px; font-weight: 600; line-height: 1.2; }
  .tagline-sub { font-size: 18px; font-weight: 300; margin-top: 4px; }
</style>
</head>
<body>
  <div class="cover">
    <svg class="cover-art" width="580" height="820" viewBox="0 0 580 820">
      <defs>
        <linearGradient id="photoTone" x1="0" y1="0" x2="1" y2="1">
          <stop offset="0" stop-color="var(--photo-light)"/>
          <stop offset=".35" stop-color="var(--photo-mid)"/>
          <stop offset=".7" stop-color="var(--photo-dark)"/>
          <stop offset="1" stop-color="var(--photo-light)"/>
        </linearGradient>
      </defs>
      <g role="img" aria-label="Foto: grüne Laborröhrchen mit DNA-Doppelhelix und gestapelte Analyseboxen">
        <path d="M0 215 L580 150 L580 820 L0 820 Z" fill="url(#photoTone)"/>
      </g>
      <path d="M0 590 C180 520 380 470 580 430 L580 560 C400 600 200 650 0 720 Z" fill="var(--teal)" opacity=".35"/>
      <path d="M0 660 C200 615 400 575 580 545 L580 820 L0 820 Z" fill="var(--green-band)"/>
      <circle class="seal" cx="490" cy="622" r="52" fill="none" stroke="var(--white)" stroke-width="2"/>
    </svg>

    <div class="brand">
      <span class="brand-dot"></span>
      <span class="brand-name">Vitalquell Nord</span>
    </div>

    <h1 class="headline">Die Zukunft<br>der Vorsorge</h1>

    <div class="tagline-block">
      <p class="tagline-main">Die auf Sie zugeschnittene<br>Mikronährstoffanalyse</p>
      <p class="tagline-sub">mit individueller Nährstoffempfehlung</p>
    </div>
  </div>
</body>
</html>
```